"Porch & Pocket" Book Cover 5.5x8.5

Title of the book is "Porch & Pocket"
Subtitle is "Untangling Ledger Myths"
I've used PixelQuarry on multiple occasions you can look on my Brindle page, Mark Teveroff, to see the covers I've used in the other projects I've done.
The target audience are people who have been tricked to think they can't retire because inflation, i.e. cost of living is going up so much they must work to keep up. There is no evidence of this.
And those are the people I want to reach so they can "Porch...and Pocket."
Target Market(s)
Americans aged 55 and over who are thinking about retirement
Industry/Entity Type
Financial
Requirements
Nice to have
- Keep It Simple, Stupid is my mantra. Just make it pop out when people are browsing
Should not have
- No piggy banks. No old people sitting on a beach.

```html
<!DOCTYPE html>
<html lang="en">
<head>
<meta charset="utf-8">
<title>Porch &amp; Pocket — Book Cover</title>
<link rel="stylesheet" href="https://fonts.googleapis.com/css2?family=Archivo+Black&family=Archivo:wght@700&family=Encode+Sans+Condensed:wght@500&display=swap">
<style>
  :root {
    --water: #1fc3d8;
    --water-light: #4fd6e8;
    --forest: #2f7a2a;
    --forest-dark: #1d5a1e;
    --title: #eef48c;
    --title-low: #e4f290;
    --ink: #363c47;
    --band: rgba(236, 234, 214, 0.94);
  }
  html, body {
    margin: 0;
    padding: 0;
    overflow: hidden;
    background: #ffffff;
  }
  .cover {
    position: relative;
    width: 750px;
    height: 1200px;
    overflow: hidden;
  }
  .cover-art {
    position: absolute;
    inset: 0;
    background:
      linear-gradient(122deg,
        var(--forest-dark) 0%,
        var(--forest) 40%,
        #3a9b6a 47%,
        var(--water) 53%,
        var(--water) 80%,
        var(--water-light) 100%);
  }
  .title {
    position: absolute;
    left: 0;
    width: 100%;
    margin: 0;
    text-align: center;
    font-family: "Archivo Black", sans-serif;
    font-weight: 400;
    line-height: 1;
  }
  .title-word {
    display: block;
    font-size: 136px;
    color: var(--title);
  }
  .title-word--top {
    position: absolute;
    top: 62px;
    left: 0;
    width: 100%;
    letter-spacing: 16px;
    padding-left: 16px;
    box-sizing: border-box;
  }
  .title-word--bottom {
    position: absolute;
    top: 240px;
    left: 0;
    width: 100%;
    letter-spacing: 2px;
    color: var(--title-low);
  }
  .title-amp {
    position: absolute;
    top: 186px;
    left: 0;
    width: 100%;
    font-size: 66px;
    color: var(--title);
  }
  .title-rule {
    position: absolute;
    top: 218px;
    height: 3px;
    background: var(--title);
  }
  .title-rule--left { left: 70px; width: 240px; background: linear-gradient(90deg, transparent, var(--title) 12%); }
  .title-rule--right { left: 440px; width: 245px; background: linear-gradient(90deg, var(--title) 88%, transparent); }
  .subtitle {
    position: absolute;
    top: 402px;
    left: 0;
    width: 100%;
    margin: 0;
    text-align: center;
    font-family: "Archivo", sans-serif;
    font-weight: 700;
    font-size: 28px;
    letter-spacing: 6px;
    color: var(--ink);
  }
  .author-band {
    position: absolute;
    left: 0;
    bottom: 0;
    width: 100%;
    height: 160px;
    background: var(--band);
    display: flex;
    align-items: center;
    justify-content: center;
  }
  .author {
    margin: 0;
    font-family: "Encode Sans Condensed", sans-serif;
    font-weight: 500;
    font-size: 86px;
    letter-spacing: -4px;
    color: var(--ink);
  }
</style>
</head>
<body>
  <main class="cover">
    <div class="cover-art" role="img" aria-label="Aerial photo of a turquoise lake meeting a dense green forest along a diagonal shoreline"></div>

    <h1 class="title">
      <span class="title-word title-word--top">PORCH</span>
      <span class="title-rule title-rule--left"></span>
      <span class="title-amp">&amp;</span>
      <span class="title-rule title-rule--right"></span>
      <span class="title-word title-word--bottom">POCKET</span>
    </h1>

    <p class="subtitle">UNTANGLING LEDGER MYTHS</p>

    <footer class="author-band">
      <p class="author">MARK TEVEROFF</p>
    </footer>
  </main>
</body>
</html>
```